New layout on letterheads, businesscards, flyers, brochures etc.

Dear Sir,
We would like to change our layout a bit. We would like to have the same look on everything we make and still keep our logo. We would like some suggestions suitable for a company like ours, where solar systems, heat pumps and LED lighting is reflected. We like our blue colour in our logo (#009ddf) and some of the black reflected in our solar panels and we like the solar cell (almost square with soft corners). We like soft lines, clean look and reflecting expensive solar panels from the very best distributors (RV, Korvantaku, Umbra Kestrel etc.). We want a light, soft, exclusive and expensive look to it all. We need this for business cards, letterhead/bottom, flyers, brochures and stickers etc.
Thank you in advance.

Tavix
Holmvej 38 B
8615 Kilmarby
Denmark

info@tavix-energi.dk
www.tavix-energi.dk

```html
<!DOCTYPE html>
<html lang="da">
<head>
<meta charset="utf-8">
<title>Tavix – Business Card</title>
<link rel="stylesheet" href="https://fonts.googleapis.com/css2?family=Roboto:wght@400;500;700&display=swap">
<style>
  :root {
    --brand-blue: #009ddf;
    --logo-grey: #8a8d90;
    --ink: #262626;
    --rule: #8c857c;
    --sun-light: #fff6d8;
    --sun-warm: #f4d9a4;
    --panel-peach: #e9c3a5;
    --panel-dusk: #b98e7a;
  }
  html, body {
    margin: 0;
    padding: 0;
    overflow: hidden;
    background: #ffffff;
  }
  .card {
    position: relative;
    width: 1200px;
    height: 733px;
    overflow: hidden;
    font-family: "Roboto", "Helvetica Neue", Arial, sans-serif;
    color: var(--ink);
  }
  .card__backdrop {
    position: absolute;
    inset: 0;
    background:
      radial-gradient(ellipse 60% 70% at 12% 18%, #fffdf3 0%, rgba(255,250,230,0.85) 35%, rgba(255,250,230,0) 70%),
      linear-gradient(120deg, var(--sun-light) 0%, var(--sun-warm) 38%, var(--panel-peach) 68%, var(--panel-dusk) 100%);
  }
  .brand {
    position: absolute;
    left: 67px;
    top: 96px;
    display: flex;
    align-items: center;
    gap: 28px;
  }
  .brand__mark {
    width: 110px;
    height: 110px;
    border-radius: 22px;
    background: var(--brand-blue);
  }
  .brand__name {
    font-size: 112px;
    font-weight: 700;
    line-height: 1;
    color: var(--logo-grey);
    letter-spacing: 2px;
  }
  .rule {
    position: absolute;
    left: 67px;
    width: 946px;
    height: 1.5px;
    background: var(--rule);
  }
  .rule--top { top: 324px; }
  .rule--mid { top: 561px; }
  .rule--bottom { top: 685px; }
  .contact {
    position: absolute;
    left: 67px;
    margin: 0;
    white-space: nowrap;
    line-height: 1;
    font-size: 43px;
  }
  .contact--name { top: 356px; font-weight: 500; }
  .contact--email { top: 423px; font-weight: 500; }
  .contact--mobile { top: 492px; font-weight: 400; }
  .company {
    position: absolute;
    left: 67px;
    margin: 0;
    white-space: nowrap;
    font-size: 32px;
    font-weight: 400;
    line-height: 1;
  }
  .company--address { top: 585px; }
  .company--lines { top: 636px; }
  .company--lines span + span { margin-left: 14px; }
</style>
</head>
<body>
  <main class="card">
    <div class="card__backdrop" role="img" aria-label="Sunlit close-up of premium solar panel cells in warm golden tones"></div>

    <div class="brand">
      <div class="brand__mark"></div>
      <div class="brand__name">Tavix</div>
    </div>

    <div class="rule rule--top"></div>

    <p class="contact contact--name">Lene Dahlqvist Mortensen</p>
    <p class="contact contact--email">l.dahlqvistmortensen@tavix-energi.dk</p>
    <p class="contact contact--mobile">M +45 20 00 300 000</p>

    <div class="rule rule--mid"></div>

    <p class="company company--address">Holmvej 38 B, 8615 Kilmarby, Denmark</p>
    <p class="company company--lines"><span>P +45 70 00 18 00</span><span>info@tavix-energi.dk</span><span>www.tavix-energi.dk</span></p>

    <div class="rule rule--bottom"></div>
  </main>
</body>
</html>
```